New Flyer Design Project

We need a flyer for our upcoming Rising Builders Forum.

5th Annual Rising Builders Forum
by the Council for Stewardship of Built Ventures (C-SBuV)
Theme: Step Forward
Date: January 24, 2020
Location: Bluestone Lodge Hotel and Conference Center, San Marcos, TX
#StepForward

This is event is put together by C-SBuV's Rising Builders Ring of Merit. I have a logo for the Ring of Merit, but not something that indicates it's the Rising Builders Ring.

More about the Forum (please don't include on the flyer): This Forum provides a venue to openly discuss issues affecting women in our industry and ideas and strategies to address those issues.

Architecture, Construction and Engineering are all struggling with a tremendous shortage of skilled talent. It is more important than ever for organizations to be able to attract, support and retain a talented workforce and to encourage more women to pursue and build vibrant careers in architecture, engineering and construction. Unfortunately, their attrition rate also remains high in these industries. Developing and retaining a skilled workforce includes identifying and addressing the specific needs of women in our industry. Man or Woman; Male or Female Brain, C-SBuV’s Rising Builders Forum will give you and your team the tools you need to excel as an Employer of Choice and a roadmap for individual continued career planning and success .

This unique Forum provides a venue to engage everyone from executives to those just beginning their careers with active, hands-on sessions and vibrant networking with the best and brightest in the A/E/C industry. In our usual C-SBuV Forum style, Keynotes become table participants and table participants become presenters, encouraging participants to assimilate what they are learning. Join local, state and national leaders and subject matter experts as we candidly explore and address the issues affecting women in our industry .

```html
<!DOCTYPE html>
<html lang="en">
<head>
<meta charset="utf-8">
<title>Rising Builders Forum – Flyer</title>
<link href="https://fonts.googleapis.com/css2?family=Montserrat:wght@800;900&family=Raleway:wght@400;500;600;700&family=Silkscreen:wght@400;700&display=swap" rel="stylesheet">
<style>
  :root {
    --page-bg: #959595;
    --ink-white: #ffffff;
    --deep-black: #05070c;
    --night-blue: #0b1a3a;
    --glow-blue: #3f8ff0;
    --glow-cyan: #a9dcff;
    --warm-glow: #e7a45a;
    --rainbow-pink: #f38ae8;
    --rainbow-violet: #a9a2ff;
    --rainbow-cyan: #7fe4ee;
    --rainbow-green: #a8f0a0;
    --rainbow-yellow: #f4ee8c;
    --rule: rgba(255,255,255,0.85);
  }
  * { margin: 0; padding: 0; box-sizing: border-box; }
  html, body { width: 1200px; height: 1123px; overflow: hidden; }
  body { background: var(--page-bg); position: relative; font-family: 'Raleway', sans-serif; }

  .flyer {
    position: absolute; left: 0; top: 139px;
    width: 1200px; height: 845px; overflow: hidden;
    background: var(--deep-black);
    color: var(--ink-white);
  }
  .hero-photo {
    position: absolute; inset: 0;
    background:
      radial-gradient(ellipse 260px 200px at 280px 360px, rgba(210,236,255,0.9), rgba(120,180,255,0.35) 55%, transparent 80%),
      radial-gradient(ellipse 120px 90px at 310px 440px, rgba(231,164,90,0.55), transparent 75%),
      radial-gradient(ellipse 420px 330px at 330px 450px, rgba(63,143,240,0.75), transparent 85%),
      radial-gradient(ellipse 300px 160px at 700px 560px, rgba(90,110,160,0.6), transparent 80%),
      linear-gradient(100deg, var(--night-blue) 0%, #123a86 25%, #0d2252 50%, #070b16 72%, var(--deep-black) 100%);
  }

  .headline {
    position: absolute; left: 50px; top: 52px;
    transform-origin: left top; transform: rotate(24.5deg);
    font-family: 'Montserrat', sans-serif; font-weight: 900;
    font-size: 74px; letter-spacing: 0; line-height: 1;
    white-space: nowrap; text-transform: uppercase;
    text-shadow: 0 0 18px rgba(0,0,0,0.35);
  }
  .headline-byline {
    position: absolute; left: 200px; top: 82px;
    transform-origin: left top; transform: rotate(22.8deg);
    font-family: 'Raleway', sans-serif; font-weight: 600;
    font-size: 20px; white-space: nowrap;
    background: linear-gradient(90deg, var(--rainbow-pink), var(--rainbow-violet), var(--rainbow-cyan), var(--rainbow-green), var(--rainbow-yellow));
    -webkit-background-clip: text; background-clip: text; color: transparent;
  }

  .event-info {
    position: absolute; left: 794px; top: 54px; width: 330px;
    text-align: center;
  }
  .edition { font-size: 37px; font-weight: 600; line-height: 1; }
  .edition sup { font-size: 22px; vertical-align: 15px; }
  .rule { height: 1px; background: var(--rule); margin: 0 auto; width: 330px; }
  .rule--top { margin-top: 18px; }
  .forum-title { display: block; margin-top: 20px; }
  .forum-title svg { display: block; width: 330px; height: 84px; }
  .forum-title text { font-family: 'Silkscreen', sans-serif; font-weight: 400; }
  .event-date {
    font-family: 'Montserrat', sans-serif; font-weight: 800;
    font-size: 23px; letter-spacing: 0.5px; margin: 22px 0 18px;
  }
  .venue { margin-top: 22px; font-size: 25px; font-weight: 400; line-height: 1.04; }
  .venue-city { display: block; font-size: 28px; font-weight: 600; margin-top: 7px; }

  .hashtag {
    position: absolute; left: 609px; top: 757px; transform: translateX(-50%);
    font-family: 'Raleway', sans-serif; font-weight: 700; font-size: 27px;
    background: linear-gradient(90deg, var(--rainbow-pink), var(--rainbow-violet), var(--rainbow-cyan), var(--rainbow-green));
    -webkit-background-clip: text; background-clip: text; color: transparent;
  }

  .org-mark {
    position: absolute; display: flex; flex-direction: column; align-items: center;
    transform: translateX(-50%); color: var(--ink-white);
    font-family: 'Raleway', sans-serif; font-weight: 500; white-space: nowrap;
  }
  .org-mark__dot { width: 56px; height: 56px; border-radius: 50%; background: var(--ink-white); margin-bottom: 12px; }
  .org-mark--council { left: 860px; top: 668px; font-size: 30px; }
  .org-mark--ring { left: 1057px; top: 674px; font-size: 24px; }
</style>
</head>
<body>
  <main class="flyer">
    <div class="hero-photo" role="img" aria-label="Photo: businesswoman in a beige suit, seen from behind, facing glowing holographic data screens and a miniature industrial plant on a floating platform"></div>

    <div class="headline-byline">by the Council for Stewardship of Built Ventures (C-SBuV)</div>
    <h1 class="headline">Rising Builders</h1>

    <section class="event-info">
      <p class="edition">5<sup>th</sup> Annual</p>
      <div class="rule rule--top"></div>
      <h2 class="forum-title" aria-label="FORUM">
        <svg viewBox="0 0 330 84" aria-hidden="true">
          <defs>
            <linearGradient id="forum-rainbow" x1="0" y1="0" x2="1" y2="0">
              <stop offset="0" stop-color="#f38ae8"/>
              <stop offset="0.3" stop-color="#a9a2ff"/>
              <stop offset="0.55" stop-color="#7fe4ee"/>
              <stop offset="0.8" stop-color="#a8f0a0"/>
              <stop offset="1" stop-color="#f4ee8c"/>
            </linearGradient>
          </defs>
          <text x="0" y="82" font-size="128" textLength="330" lengthAdjust="spacingAndGlyphs" fill="url(#forum-rainbow)">FORUM</text>
        </svg>
      </h2>
      <p class="event-date">JANUARY 24, 2020</p>
      <div class="rule"></div>
      <p class="venue">Bluestone Lodge Hotel and Conference Center,<span class="venue-city">San Marcos, TX</span></p>
    </section>

    <p class="hashtag">#StepForward</p>

    <div class="org-mark org-mark--council">
      <span class="org-mark__dot"></span>
      <span>C-SBuV</span>
    </div>
    <div class="org-mark org-mark--ring">
      <span class="org-mark__dot"></span>
      <span>Ring of Merit</span>
    </div>
  </main>
</body>
</html>
```